Banner Ad Design Project

I require banner ad designs with the below wording.

1. Join Today and Make Money Tomorrow. Unlimited Income. Click Here Now

2. I lost my job. Now I Make Over $5,000 Per Week From Home. You Can Too. Free Info, Apply Now

I require sizes: 300x250 and 728x90 and 468x60 and 120x240

The design should communicate legitimate, accredited, online business.

Industry/Entity Type

Business

Requirements
Should not have
• Creative attributes to avoid*
Phone numbers in creative
Creative with no click buttons
Interactive creative
Brand messaging with no call to action
Creative with long looping times

```html
<!DOCTYPE html>
<html lang="en">
<head>
<meta charset="utf-8">
<title>Income Opportunity Banner Set</title>
<link rel="stylesheet" href="https://fonts.googleapis.com/css2?family=Francois+One&family=Roboto+Condensed:wght@400;700&family=Playfair+Display:ital@1&display=swap">
<style>
  :root {
    --stage: #a8a8a8;
    --stage-light: #c4c4c4;
    --ink-black: #0d0d0d;
    --ink-charcoal: #3a3a3a;
    --berry: #c8124f;
    --berry-deep: #9c0a3a;
    --berry-light: #e0306b;
    --gold-top: #fff27a;
    --gold-bottom: #e8b514;
    --white: #ffffff;
    --photo-warm: #d9c2b4;
    --photo-cool: #e9e4e4;
    --cash: #b9c2ab;
  }
  html, body {
    margin: 0;
    width: 1200px;
    height: 900px;
    overflow: hidden;
  }
  body {
    position: relative;
    background: radial-gradient(ellipse at 50% 40%, var(--stage-light), var(--stage) 75%);
  }
  .banner {
    position: absolute;
    display: block;
    box-shadow: 0 2px 5px rgba(0,0,0,.35);
  }
  .banner--rect-join { left: 102px; top: 63px; width: 450px; height: 375px; }
  .banner--rect-story { left: 636px; top: 63px; width: 450px; height: 375px; }
  .banner--leader-join { left: 37px; top: 502px; width: 1094px; height: 135px; }
  .banner--leader-story { left: 37px; top: 670px; width: 1094px; height: 135px; }

  .headline-gold { font-family: "Francois One", "Roboto Condensed", sans-serif; fill: url(#goldText); }
  .body-sans { font-family: "Roboto Condensed", sans-serif; }
  .script-serif { font-family: "Playfair Display", serif; font-style: italic; }
</style>
</head>
<body>

<svg width="0" height="0" style="position:absolute" aria-hidden="true">
  <defs>
    <linearGradient id="goldText" x1="0" y1="0" x2="0" y2="1">
      <stop offset="0" stop-color="var(--gold-top)"/>
      <stop offset="1" stop-color="var(--gold-bottom)"/>
    </linearGradient>
    <linearGradient id="darkPanel" x1="0" y1="0" x2="1" y2="0">
      <stop offset="0" stop-color="var(--ink-charcoal)"/>
      <stop offset="1" stop-color="var(--ink-black)"/>
    </linearGradient>
    <linearGradient id="berryPanel" x1="0" y1="0" x2="0" y2="1">
      <stop offset="0" stop-color="var(--berry-light)"/>
      <stop offset="1" stop-color="var(--berry-deep)"/>
    </linearGradient>
    <linearGradient id="pillFill" x1="0" y1="0" x2="0" y2="1">
      <stop offset="0" stop-color="#ffffff"/>
      <stop offset="1" stop-color="#dcdcdc"/>
    </linearGradient>
  </defs>
</svg>

<!-- 300x250 : Join Today -->
<svg class="banner banner--rect-join" viewBox="0 0 300 250">
  <rect width="300" height="250" fill="url(#darkPanel)"/>
  <path d="M90 250 C160 230 230 190 300 175 L300 250 Z" fill="url(#berryPanel)"/>
  <path d="M90 250 C160 230 230 190 300 175" fill="none" stroke="var(--white)" stroke-width="2"/>
  <rect x="0" y="0" width="115" height="250" fill="var(--photo-warm)" role="img" aria-label="Photo of a smiling businesswoman in glasses"/>
  <text class="headline-gold" x="195" y="50" font-size="34" text-anchor="middle">Join Today</text>
  <text class="body-sans" x="188" y="76" font-size="15" fill="var(--white)" text-anchor="middle">&amp; Make Money  Tomorrow</text>
  <text class="script-serif" x="195" y="118" font-size="20" fill="var(--white)" text-anchor="middle">Unlimited Income</text>
  <g transform="rotate(-12 185 185)">
    <rect x="125" y="160" width="120" height="52" fill="var(--cash)" role="img" aria-label="Fanned stack of dollar bills"/>
  </g>
  <path d="M188 205 H300 V240 H188 A17.5 17.5 0 0 1 188 205 Z" fill="url(#pillFill)"/>
  <text class="body-sans" x="236" y="228" font-size="15" fill="var(--ink-black)" text-anchor="middle">Click Here Now</text>
</svg>

<!-- 300x250 : Story -->
<svg class="banner banner--rect-story" viewBox="0 0 300 250">
  <rect width="300" height="250" fill="url(#berryPanel)"/>
  <path d="M0 0 H300 V95 C200 70 120 60 40 95 C20 60 10 30 0 20 Z" fill="var(--photo-cool)" role="img" aria-label="Photo of a joyful woman in a business suit throwing her arms up"/>
  <path d="M40 95 C120 60 200 70 300 95" fill="none" stroke="var(--berry-deep)" stroke-width="4"/>
  <text class="body-sans" x="150" y="130" font-size="18" fill="var(--white)" text-anchor="middle">I lost my job. Now I Make Over</text>
  <text class="headline-gold" x="150" y="162" font-size="27" text-anchor="middle">$5,000 Per Week</text>
  <text class="body-sans" x="150" y="192" font-size="18" fill="var(--white)" text-anchor="middle">From Home</text>
  <path d="M0 215 C100 198 200 198 300 212 V250 H0 Z" fill="var(--white)"/>
  <text class="body-sans" x="150" y="236" font-size="15.5" fill="var(--berry)" text-anchor="middle">You Can Too. Free Info, Apply Now</text>
</svg>

<!-- 728x90 : Join Today -->
<svg class="banner banner--leader-join" viewBox="0 0 729 90">
  <rect width="729" height="90" fill="url(#berryPanel)"/>
  <path d="M0 0 H420 C400 30 400 60 430 90 H0 Z" fill="url(#darkPanel)"/>
  <rect x="0" y="0" width="60" height="90" fill="var(--photo-warm)" role="img" aria-label="Photo of a smiling businesswoman in glasses"/>
  <text class="headline-gold" x="72" y="49" font-size="44">Join Today</text>
  <text class="body-sans" x="75" y="76" font-size="17" fill="var(--white)">&amp; Make Money  Tomorrow</text>
  <g transform="rotate(-10 372 45)">
    <rect x="305" y="10" width="135" height="68" fill="var(--cash)" role="img" aria-label="Fanned stack of dollar bills"/>
  </g>
  <text class="script-serif" x="512" y="40" font-size="28" fill="var(--white)" text-anchor="middle">Unlimited</text>
  <text class="script-serif" x="512" y="72" font-size="28" fill="var(--white)" text-anchor="middle">Income</text>
  <path d="M612 20 H729 V72 H612 A26 26 0 0 1 612 20 Z" fill="url(#pillFill)"/>
  <text class="body-sans" x="660" y="53" font-size="19" fill="var(--ink-black)" text-anchor="middle">Click Here Now</text>
</svg>

<!-- 728x90 : Story -->
<svg class="banner banner--leader-story" viewBox="0 0 729 90">
  <rect width="729" height="90" fill="var(--white)"/>
  <rect x="0" y="0" width="160" height="90" fill="var(--photo-cool)" role="img" aria-label="Photo of a joyful woman in a business suit throwing her arms up"/>
  <path d="M135 0 H445 L458 45 L445 90 H100 C140 70 150 30 135 0 Z" fill="url(#berryPanel)"/>
  <path d="M711 0 H729 V90 H711 L724 45 Z" fill="url(#berryPanel)"/>
  <text class="body-sans" x="298" y="24" font-size="17" fill="var(--white)" text-anchor="middle">I lost my job Now I Make Over</text>
  <text class="headline-gold" x="298" y="55" font-size="26" text-anchor="middle">$5,000 Per Week</text>
  <text class="body-sans" x="298" y="81" font-size="16" fill="var(--white)" text-anchor="middle">From Home</text>
  <text class="body-sans" x="590" y="37" font-size="22" fill="var(--berry)" text-anchor="middle">You Can Too</text>
  <text class="body-sans" x="590" y="68" font-size="22" fill="var(--berry)" text-anchor="middle">Free Info, Apply Now</text>
</svg>

</body>
</html>
```